PowerPoint template for project mangement course material

I need a ppt template for the slides at our project management course. IT should be arather simple adn stylish not taking the focus away from the content. We are two companies delivering the course - thus the template should be held in the colours of the two companies and their logos. we need different layouts for the template - the logos should be included in minimum the title layout.
The content is a mix of text and figures.
(uploaded ppt shows an example of the content)

Industry/Entity Type

Training

Font styles to use
Serif
Sans Serif

Requirements
Must have
• different layouts: title, section, standard, two columns, headline only etc.
Nice to have
• nice bullets, mostly white background

```html
<!DOCTYPE html>
<html lang="da">
<head>
<meta charset="utf-8">
<title>Projektledelse i praksis – skabelon</title>
<link href="https://fonts.googleapis.com/css2?family=Bebas+Neue&family=Open+Sans:wght@300;400;600&display=swap" rel="stylesheet">
<style>
:root{
  --navy:#1f3f7f;
  --navy-dark:#16305f;
  --blue:#2b56a0;
  --red:#a3302c;
  --red-dark:#8c2724;
  --ink:#222;
  --grey-bg:#ececec;
  --slide-bg:#f4f4f4;
  --label:#555;
}
*{box-sizing:border-box;margin:0;padding:0}
html,body{width:1200px;height:1026px;overflow:hidden}
body{background:linear-gradient(#f7f7f7,#e9e9e9);font-family:"Open Sans",sans-serif;color:var(--ink);position:relative}
.slide{position:absolute;width:568px;height:426px;background:linear-gradient(#fafafa,#ececec);box-shadow:0 2px 8px rgba(0,0,0,.25);overflow:hidden}
.s1{left:16px;top:38px}.s2{left:614px;top:38px}.s3{left:16px;top:536px}.s4{left:614px;top:536px}
.page-label{position:absolute;width:568px;text-align:center;font-size:21px;color:var(--label)}
.top-band{position:absolute;left:0;top:0;width:100%;height:8px;background:linear-gradient(90deg,var(--navy-dark),var(--blue),var(--navy-dark))}
.footer{position:absolute;left:0;bottom:8px;width:100%;height:23px;border-top:1.5px solid var(--navy);display:flex;align-items:center;justify-content:space-between;padding:0 23px 0 22px;font-size:8.4px;color:#111}
.bottom-band{position:absolute;left:0;bottom:0;width:100%;height:8px;background:linear-gradient(90deg,var(--navy-dark),var(--blue),var(--navy-dark))}
.headline{font-family:"Bebas Neue",sans-serif;font-weight:400;letter-spacing:.3px}
.slide-title{position:absolute;left:22px;top:22px;font-size:31px;color:var(--red);line-height:1}
.title-rule{position:absolute;left:22px;top:52px;width:64px;height:3px;background:var(--navy)}
.photo{position:absolute}
/* title slide */
.cover-text{position:absolute;left:0;width:100%;text-align:center;color:#fff}
.cover-title{top:48px;font-size:41px;line-height:1}
.cover-sub{top:100px;font-size:16.5px;font-weight:300;letter-spacing:.3px}
.cover-rule{position:absolute;left:246px;top:133px;width:96px;height:2px;background:#fff}
.cover-day{top:146px;font-size:37px;line-height:1}
.partner{position:absolute;display:flex;flex-direction:column}
.partner-a{left:24px;top:328px}
.partner-b{right:26px;top:330px;align-items:flex-end}
.partner-row{display:flex;align-items:center;gap:6px}
.partner-name{font-size:28px;font-weight:400;line-height:1;color:#4a4a4a}
.partner-b .partner-name{color:var(--navy)}
.partner-mark{width:12px;height:12px;background:var(--red)}
.partner-mark.round{border-radius:50%;background:var(--navy)}
.partner-tag{font-size:9.5px;color:#666;letter-spacing:.5px;margin-top:2px}
.partner-b .partner-tag{font-size:13px;color:var(--navy);letter-spacing:.3px}
/* welcome */
.body-copy{position:absolute;left:22px;width:523px;font-size:9.9px;line-height:13.5px;text-align:justify;color:#222}
.body-copy p+p{margin-top:7px}
/* purpose */
.purpose-box{position:absolute;left:0;top:84px;width:210px;height:241px;background:rgba(163,48,44,.93);color:#fff;padding:14px 14px 0 22px}
.purpose-box h2{font-size:33px;line-height:1;font-weight:400}
.purpose-box .rule{width:66px;height:2px;background:#fff;margin:8px 0 12px}
.purpose-box p{font-size:9.9px;line-height:13.4px;margin-bottom:9px}
/* contents */
.col{position:absolute;top:66px;height:318px;width:125px}
.col-photo{left:20px}.col-m1{left:152px}.col-photo2{left:284px}.col-m2{left:416px;width:133px}
.module{background:var(--red);color:#fff;text-align:center;padding:11px 6px 0}
.module h3{font-weight:300;font-size:17px;letter-spacing:.3px;line-height:1}
.module svg{display:block;margin:10px auto 9px}
.module ul{list-style:none;font-size:9.7px;line-height:13px}
.module li{margin-bottom:9.8px}
.module li.bullet::before{content:"• "}
</style>
</head>
<body>

<!-- Slide 1: title -->
<section class="slide s1">
  <svg class="photo" width="568" height="426" viewBox="0 0 568 426" role="img" aria-label="Foto af hænder ved en bærbar computer, tonet i blåt">
    <defs>
      <linearGradient id="coverBlue" x1="0" y1="0" x2="1" y2="1">
        <stop offset="0" stop-color="#2a4f94"/><stop offset=".6" stop-color="#244785"/><stop offset="1" stop-color="#1b3a73"/>
      </linearGradient>
    </defs>
    <path d="M0 0H568V292C500 320 410 312 320 270C250 236 150 200 80 230C40 248 15 268 0 290Z" fill="url(#coverBlue)"/>
    <path d="M0 292C40 240 110 200 200 206C290 212 380 250 460 262C510 270 545 262 568 250" fill="none" stroke="#a3302c" stroke-width="6"/>
    <path d="M0 300C45 250 115 212 205 216C295 220 385 262 465 274C515 280 548 272 568 262" fill="none" stroke="#fff" stroke-width="2"/>
  </svg>
  <div class="top-band"></div>
  <h1 class="cover-text cover-title headline">Projektledelse i praksis</h1>
  <p class="cover-text cover-sub">MODUL 2 – LEDELSE OG GENNEMFØRELSE</p>
  <div class="cover-rule"></div>
  <p class="cover-text cover-day headline">Dag 1</p>
  <div class="partner partner-a">
    <div class="partner-row"><span class="partner-mark"></span><span class="partner-name">waypoint</span></div>
    <span class="partner-tag">lead plan deliver</span>
  </div>
  <div class="partner partner-b">
    <div class="partner-row"><span class="partner-mark round"></span><span class="partner-name">Norvik</span></div>
    <span class="partner-tag">konsulentfirma</span>
  </div>
  <footer class="footer"><span>27-06-2017</span><span>Projektledelse i praksis v. Ida Halvorsen og Sofie Lindberg</span><span>Page No. - 01</span></footer>
  <div class="bottom-band"></div>
</section>
<div class="page-label" style="left:16px;top:478px">Page 1</div>

<!-- Slide 2: welcome -->
<section class="slide s2">
  <div class="top-band"></div>
  <h2 class="slide-title headline">Velkommen</h2>
  <div class="title-rule"></div>
  <div class="photo" style="left:22px;top:72px;width:523px;height:160px;background:linear-gradient(110deg,#6b5a4a 0%,#8f8d8c 30%,#b7b8ba 55%,#3a3530 100%);border-bottom:5px solid var(--red)" role="img" aria-label="Foto af bærbar computer, notesbog og kuglepen på et træbord"></div>
  <div class="body-copy" style="top:256px">
    <p>Lorem Ipsum is simply dummy text of the printing and typesetting industry. Lorem Ipsum has been the industry's standard dummy text ever since the 1500s, when an unknown printer took a galley of type and scrambled it to make a type specimen book. It has survived not only five centuries, but also the leap into electronic typesetting, remaining essentially unchanged. It was popularised in the 1960s with the release of Letraset sheets containing.</p>
    <p>Lorem Ipsum is simply dummy text of the printing and typesetting industry. Lorem Ipsum has been the industry's standard dummy text ever since the 1500s, when an unknown printer took a galley of type and scrambled it to make a type specimen book. It has survived not only five centuries, but also the leap into electronic typesetting. when an unknown printer took a galley of type and scrambled it to make a type specimen book. It has survived not only five centuries, but also the leap into electronic typesetting.when an unknown printer took a galley of type.</p>
  </div>
  <footer class="footer"><span>27-06-2017</span><span>Projektledelse i praksis v. Ida Halvorsen og Sofie Lindberg</span><span>Page No. - 02</span></footer>
  <div class="bottom-band"></div>
</section>
<div class="page-label" style="left:614px;top:478px">Page 2</div>

<!-- Slide 3: purpose -->
<section class="slide s3">
  <div class="top-band"></div>
  <div class="photo" style="left:0;top:14px;width:568px;height:376px;background:linear-gradient(135deg,#7f9692 0%,#c9d1cf 40%,#9fb0ad 70%,#3e4a4c 100%)" role="img" aria-label="Foto af to personer der tegner skitser ved bærbare computere"></div>
  <div class="purpose-box">
    <h2 class="headline">Formål med<br>kurset</h2>
    <div class="rule"></div>
    <p>At give deltagerne en grundlæggende viden og forståelse for at arbejde som projektleder</p>
    <p>samt</p>
    <p>formidle og diskutere en række projektledelsesværktøjer i relation til deltagernes egne projekter.</p>
  </div>
  <footer class="footer"><span>27-06-2017</span><span>Projektledelse i praksis v. Ida Halvorsen og Sofie Lindberg</span><span>Page No. - 03</span></footer>
  <div class="bottom-band"></div>
</section>
<div class="page-label" style="left:16px;top:976px">Page 3</div>

<!-- Slide 4: contents -->
<section class="slide s4">
  <div class="top-band"></div>
  <h2 class="slide-title headline">Indhold på kurset</h2>
  <div class="title-rule"></div>
  <div class="col col-photo" style="background:linear-gradient(180deg,#c9a7c4,#9b7a9a 60%,#b595b0)" role="img" aria-label="Silhuet af en forretningsmand foran pengesedler"></div>
  <div class="col col-m1 module">
    <h3>MODUL 1</h3>
    <svg width="44" height="44" viewBox="0 0 44 44" aria-hidden="true">
      <circle cx="22" cy="22" r="22" fill="#fff"/>
      <path d="M9 22l7-7 6 4 6-4 7 7-8 8-5-4-5 4z" fill="#2b56a0"/>
    </svg>
    <ul>
      <li>Grundforståelse – få styr på projektet</li>
      <li class="bullet">Projektets natur og karakteristika</li>
      <li class="bullet">Roller</li>
      <li class="bullet">Relationer</li>
      <li class="bullet">Risici</li>
      <li class="bullet">Planlægning</li>
      <li class="bullet">Kommunikation</li>
    </ul>
  </div>
  <div class="col col-photo2" style="background:linear-gradient(160deg,#2a2a2a,#555 40%,#d9d9d9 60%,#3a3a3a)" role="img" aria-label="Foto af hænder der peger på et dokument med diagrammer"></div>
  <div class="col col-m2 module">
    <h3>MODUL 2</h3>
    <svg width="44" height="44" viewBox="0 0 44 44" aria-hidden="true">
      <circle cx="22" cy="22" r="22" fill="#fff"/>
      <circle cx="17" cy="17" r="5" fill="#2b56a0"/>
      <path d="M8 34c0-7 4-10 9-10s9 3 9 10z" fill="#2b56a0"/>
      <rect x="25" y="11" width="11" height="14" fill="none" stroke="#2b56a0" stroke-width="2"/>
    </svg>
    <ul>
      <li>Projektledelse i praksis</li>
      <li class="bullet">Ledelse og motivation</li>
      <li class="bullet">Styring og opfølgning i projekter</li>
      <li class="bullet">Håndtering af konflikter</li>
      <li class="bullet">Samarbejde på distance</li>
      <li class="bullet">Magt og tillid</li>
      <li class="bullet">Forhandlingsteknikker og ledelsesstile</li>
      <li class="bullet">At kommunikere målrettet</li>
    </ul>
  </div>
  <footer class="footer"><span>27-06-2017</span><span>Projektledelse i praksis v. Ida Halvorsen og Sofie Lindberg</span><span>Page No. - 04</span></footer>
  <div class="bottom-band"></div>
</section>
<div class="page-label" style="left:614px;top:976px">Page 4</div>

</body>
</html>
```